Vistalune Web Design Project

We need a new web site for our company. Vistalune provides a range of location intelligence and marketing services to assist clients in improving their performance. On the location intelligence side we're the local partner for Orbix Terra (Charts and Globe) in South Africa, we're the local reseller and can assist company with the implementation and customization - we'll shortly receive the Orbix partner logo that should also be displayed on the Homepage. On the marketing side, we provide a range of marketing services for example Tenders, Event Management and Copy writing. The company is a blend between a mapping and marketing services company. You can have a look at the existing site at www.vistalune.co.za
Updates

Dear designers, the budget for my project has been increased to $700. Looking forward to receiving your designs. Kind regards Henrik

Dear designers - many thanks for all the great designs received to date. We'll provide feedback shortly. Kind regards Vistalune

Target Market(s)

Our target market is public and private organisations, and online customers (those with a web presence) primarily in South Africa

Industry/Entity Type

Marketing

Requirements
Must have
• I have uploaded the latest text and suggested pages at this stage. Important is that it should be easy to edit the pages in an HTML editor, e.g. Pagecraft. I suspect that the navigation will be expanded later e.g. careers, success stories - so it should be easy for me add new sections to the navigation later on. I have also uploaded the different Vistalune logo designs. Please include links on the Homepage for Terms and Conditions and PAIA - see www.vistalune.co.za - also the Copyright Note at the bottom of every page
Nice to have
• Although we're targeting corporates and government, and online customers, the site should be fresh and easy to navigate. I like the use of photographs on sites and make them look more interesting than simply text. Although we're also providing marketing services, the location intelligence (mapping) and Orbix Charts/Globe aspect are perhaps the most important part of the website.

```html
<!DOCTYPE html>
<html lang="en">
<head>
<meta charset="utf-8">
<title>Vistalune – Location Intelligence &amp; Marketing</title>
<link href="https://fonts.googleapis.com/css2?family=Open+Sans:wght@300;400;600&family=Yanone+Kaffeesatz:wght@400;500&family=Maven+Pro:wght@400;500&display=swap" rel="stylesheet">
<style>
:root{
  --red:#d8161c;
  --red-dark:#a80b10;
  --slate:#434b53;
  --ink:#333;
  --muted:#666;
  --page:#ededed;
  --panel:#ebeae6;
  --white:#fff;
  --green:#6ab02c;
  --link:#5a9a1e;
  --rule:#dcdcdc;
  --hero-bg:#f4f4f4;
}
*{margin:0;padding:0;box-sizing:border-box}
html,body{width:1000px;height:1200px;overflow:hidden}
body{background:var(--page);font-family:"Open Sans",Arial,sans-serif;color:var(--ink);position:relative}
.abs{position:absolute}
.column{position:absolute;left:91px;width:817px;background:var(--white)}

/* header */
.site-header{top:0;height:185px}
.brand{left:22px;top:38px;display:flex;align-items:center;gap:10px}
.brand-dot{width:26px;height:26px;border-radius:50%;background:var(--red)}
.brand-name{font-family:"Open Sans",sans-serif;font-weight:600;font-size:36px;color:var(--slate);letter-spacing:-.5px}
.contact-top{right:14px;top:22px;text-align:right;font-family:"Yanone Kaffeesatz",sans-serif;font-size:18px;line-height:25px;color:var(--ink)}
.contact-top .label{color:var(--red)}
.follow{right:14px;top:76px;display:flex;align-items:center;gap:6px;font-family:"Yanone Kaffeesatz",sans-serif;font-size:18px}
.follow .label{color:var(--red);margin-right:4px}
.social{display:flex;align-items:center;gap:3px;font-size:13px;color:var(--slate);font-family:"Open Sans",sans-serif;white-space:nowrap}
.social i{display:block;width:10px;height:10px;background:var(--slate)}
.main-nav{left:11px;top:119px;width:799px;height:44px;border-radius:7px;background:linear-gradient(#e0242a,var(--red-dark));box-shadow:0 2px 3px rgba(0,0,0,.25)}
.main-nav ul{list-style:none;display:flex;align-items:center;height:100%;padding-left:29px}
.main-nav li{font-family:"Yanone Kaffeesatz",sans-serif;font-size:15px;color:#fff;padding:4px 12px;white-space:nowrap;letter-spacing:.2px;line-height:16px}
.main-nav li.active{background:var(--slate);border-radius:3px;padding:4px 15px}

/* hero */
.hero-band{left:0;top:185px;width:1000px;height:310px;background:var(--slate)}
.hero{left:92px;top:185px;width:816px;height:310px;background:var(--hero-bg);overflow:hidden}
.hero-photo{position:absolute;left:357px;top:0;width:459px;height:310px;background:linear-gradient(100deg,#d9d3c4 0%,#b9a98a 35%,#8f8a80 65%,#c6bfae 100%)}
.hero-photo::before{content:"";position:absolute;left:0;top:0;width:70px;height:100%;background:linear-gradient(90deg,var(--hero-bg),rgba(244,244,244,0))}
.hero-copy{position:absolute;left:17px;top:46px;font-weight:300;font-size:20px;line-height:30px;color:#444}
.hero-copy span{display:block;white-space:nowrap}
.hero-copy strong{color:var(--red);font-weight:400}
.btn-discover{position:absolute;left:17px;top:183px;padding:3px 26px 3px 8px;background:linear-gradient(#7dc238,#55981c);color:#fff;font-size:13px;border-radius:2px;letter-spacing:.3px}
.btn-discover::after{content:"";position:absolute;right:9px;top:8px;width:6px;height:6px;border-top:2px solid #222;border-right:2px solid #222;transform:rotate(45deg)}

/* welcome */
.welcome{top:495px;height:182px}
.welcome h1{position:absolute;left:12px;top:22px;font-weight:400;font-size:26px;color:#333}
.welcome h1 span{color:var(--red)}
.welcome p{position:absolute;left:11px;width:470px;font-size:10px;line-height:15px;color:var(--muted)}
.testimonial{position:absolute;left:510px;top:15px;width:270px;height:143px;background:#f6f6f6;padding:10px 18px}
.testimonial h2{font-family:"Maven Pro",sans-serif;font-weight:400;font-size:21px;color:#333;padding-bottom:6px;border-bottom:1px solid var(--rule)}
.testimonial blockquote{font-family:"Maven Pro",sans-serif;font-size:11px;line-height:15px;margin-top:8px}
.testimonial cite{display:block;font-style:normal;font-size:9px;margin-top:10px}
.testimonial a{display:block;font-size:9px;color:var(--link);margin-top:5px;text-decoration:none}

/* services */
.services{top:677px;height:256px;background:var(--panel)}
.service{position:absolute;top:0;width:196px}
.service h3{font-family:"Yanone Kaffeesatz",sans-serif;font-weight:400;font-size:21px;color:var(--slate);padding:13px 0 0 10px;height:46px;white-space:nowrap}
.service .card{background:#fff;border:1px solid #d8d8d8;height:197px;padding:3px 5px}
.service .thumb{height:74px}
.service p{font-family:"Maven Pro",sans-serif;font-size:11px;line-height:15px;color:#444;padding:6px 9px 0}

/* footer */
.footer-info{top:933px;height:228px}
.footer-col{position:absolute;top:28px}
.footer-col h4{font-family:Georgia,serif;font-weight:400;font-size:12px;color:#555;text-transform:uppercase;padding-bottom:10px;border-bottom:1px solid #e6e6e6}
.about p{font-family:Arial,sans-serif;font-size:9.5px;line-height:15px;color:#666;margin-top:16px}
.offer ul,.contact ul{list-style:none;margin-top:10px}
.offer li{font-family:Arial,sans-serif;font-size:9px;color:#777;line-height:20px}
.offer li::before,.contact li::before{content:"+ ";color:#999}
.contact li{font-family:"Yanone Kaffeesatz",sans-serif;font-size:12.5px;color:#333;line-height:22px}
.contact li a{color:#c46a10}
.btn-inquiry{display:inline-block;margin-top:10px;background:#e46a6a;color:#fff;font-family:Georgia,serif;font-weight:700;font-size:10px;padding:6px 20px 6px 11px;clip-path:polygon(0 0,88% 0,100% 50%,88% 100%,0 100%)}
.footer-social{display:flex;gap:5px;margin-top:14px;padding-top:14px;border-top:1px solid #e6e6e6}
.footer-social .social{color:#555;font-size:9px}
.site-footer{top:1161px;height:39px;background:var(--slate);color:#ddd;font-family:Arial,sans-serif;font-size:10px}
.site-footer .copy{position:absolute;left:17px;top:13px}
.site-footer .legal{position:absolute;right:17px;top:13px}
</style>
</head>
<body>

<header class="column site-header">
  <div class="abs brand"><span class="brand-dot"></span><span class="brand-name">Vistalune</span></div>
  <div class="abs contact-top">
    <div><span class="label">Call Now!</span> +27 21 555 0147</div>
    <div><span class="label">Email:</span> info@vistalune.co.za</div>
  </div>
  <div class="abs follow">
    <span class="label">Follow Us On:</span>
    <span class="social"><i></i>Feed</span>
    <span class="social"><i></i>Pageline</span>
    <span class="social"><i></i>Chirpit</span>
    <span class="social"><i></i>Linkbase</span>
  </div>
  <nav class="abs main-nav">
    <ul>
      <li class="active">HOME</li><li>ABOUT US</li><li>SERVICES</li><li>PRODUCTS</li><li>MAP OFFICE</li><li>TENDER OFFICE</li><li>SALES OFFICE</li><li>CONTENT OFFICE</li><li>EVENT OFFICE</li><li>CONTACT US</li>
    </ul>
  </nav>
</header>

<div class="abs hero-band"></div>
<section class="abs hero">
  <div class="hero-photo" role="img" aria-label="Photo of a couple of tourists reading a paper map on a sunny old-town street"></div>
  <p class="hero-copy">
    <span><strong>Vistalune</strong> provides a range of</span>
    <span>location intelligence and marketing</span>
    <span>services and products to assist clients</span>
    <span>in improving their performance.</span>
  </p>
  <span class="btn-discover">DISCOVER</span>
</section>

<section class="column welcome">
  <h1>Welcome to <span>Vista</span>lune</h1>
  <p style="top:65px">Vistalune provides a range of location intelligence and marketing services and products to assist clients in improving their performance. We enjoy challenging projects that stretch the imagination and encourage out of the box thinking.</p>
  <p style="top:125px">We have extensive experience in providing world-class service to private and public organisations, locally as well as internationally and we strive to build long-term lasting relationships with our clients.</p>
  <aside class="testimonial">
    <h2>Our Client Says...</h2>
    <blockquote>These guys did really very excellent job, I must recommend them to all. Vistalune team is honest and healthy in work progress.</blockquote>
    <cite>Tarek Naveen Osei - Co-Founder [ UAE ]</cite>
    <a href="#">www.quillbrooksystems.com</a>
  </aside>
</section>

<section class="column services">
  <div class="service" style="left:0">
    <h3>MARKETING SERVICES</h3>
    <div class="card">
      <div class="thumb" role="img" aria-label="Photo of an office worker with a headset at a computer" style="background:linear-gradient(90deg,#6d7f70,#b9c3c6,#dfe3e5)"></div>
      <p>Vistalune provides a complete turnkey solution to companies participating in government and parastatal tenders. Tailor-made tender services are also offered for companies requiring assistance</p>
    </div>
  </div>
  <div class="service" style="left:207px">
    <h3>CONSULTING</h3>
    <div class="card">
      <div class="thumb" role="img" aria-label="Photo of business consultants in suits" style="background:linear-gradient(90deg,#e9e9e9,#6b6f76,#3a3d44)"></div>
      <p>Vistalune has extensive experience in managing large complex projects, from conceptualisation to implementation and support.</p>
    </div>
  </div>
  <div class="service" style="left:415px">
    <h3>SOFTWARE DEVELOPMENT</h3>
    <div class="card">
      <div class="thumb" role="img" aria-label="Blue digital innovation illustration with a world map" style="background:linear-gradient(135deg,#0d4fa0,#2f8fe0,#0a3a7a)"></div>
      <p>Vistalune development team is well versed in deploying various system development life-cycle (SDLC) methodologies, including Waterfall, V-model, Spiral, Scrum and Rapid Application Development (RAD).</p>
    </div>
  </div>
  <div class="service" style="left:622px">
    <h3>ORBIX CHARTS FOR BUSINESS</h3>
    <div class="card">
      <div class="thumb" role="img" aria-label="Illustration of a compass and map pin on a folded map" style="background:radial-gradient(circle at 60% 50%,#2f6f9a,#b9c7c8 60%,#f3f3f1)"></div>
      <p>Vistalune is the local partner for Orbix Terra products in South Africa. Contact us for any technical, commercial or legal queries regarding these products.</p>
    </div>
  </div>
</section>

<footer class="column footer-info">
  <div class="footer-col about" style="left:10px;width:395px">
    <h4>About Us</h4>
    <p>Vistalune provides a range of location intelligence and marketing services and products to assist clients in improving their performance. We enjoy challenging projects that stretch the imagination and encourage out of the box thinking. We have extensive experience in providing world-class service to private and public organisations, locally as well as internationally and we strive to build long-term lasting relationships with our clients.</p>
  </div>
  <div class="footer-col offer" style="left:418px;width:185px">
    <h4>What We Offer</h4>
    <ul>
      <li>Developing a sales strategy</li>
      <li>Identifying the value proposition</li>
      <li>Focusing on the target market</li>
      <li>Analysing products/services</li>
      <li>Assessing operational readiness</li>
      <li>Creating a product/brand strategy</li>
    </ul>
  </div>
  <div class="footer-col contact" style="left:622px;width:190px">
    <h4>Contact Us</h4>
    <ul>
      <li>Call Now! +27 21 555 0147</li>
      <li>Email: info@vistalune.co.za</li>
      <li><a href="#">Show legal info</a></li>
    </ul>
    <span class="btn-inquiry">DESIGN INQUIRY FORM</span>
    <div class="footer-social">
      <span class="social"><i></i>Feed</span>
      <span class="social"><i></i>Pageline</span>
      <span class="social"><i></i>Chirpit</span>
      <span class="social"><i></i>Linkbase</span>
    </div>
  </div>
</footer>

<div class="column site-footer">
  <span class="copy">© Copyright 2012 Vistalune. All Rights Reserved.</span>
  <span class="legal">Terms and Conditions &nbsp;|&nbsp; Privacy Policy</span>
</div>

</body>
</html>
```